Holloway-Prentiss & Associates
Business card & Word template design
Draft #12:
I like the shading -- it gives it dimension. But I would prefer a solid blue bar along the bottom (rather than a blue /black bar). I also like the back side of the bottom card. Could you remove the words "Financial Planning & Wealth Advisors" from the logo to make it look less busy?
Draft #10: Please see comments for Draft #11, as they apply as well. I like the wave on this one! One thought - could you put the phone and fax number on the same line to reduce the number of horizontal lines and create more balance for the long email address line?
Draft #11:
Nice work! I like the placement of the logo on the all-cap version (the design that has the logo on the left and more centered vertically). I like the shape of the all-cap letters but they seem lighter and not as easy to read(don't pop out as much as the other font). Could I please see a version that has the non-cap (darker) font on the layout with the logo on the left? Also, could you remove the word "email" from before the email address?
Draft #18 - additional note -- could you also please remove the comma after "Suite 485" in the address if it's on two different lines?
Draft #18:
Nice work! I like the blue area. I don't need the URL on the card, but I do need the words "Registered Investment Advisor" and "Financial Planning & Fee-Only Investments". Also, I like the line spacing on the address better than the line spacing on the phone/fax/email side of the card.
Nice work!
I am a little concerned with font being too small or narrow to be easily readable. I would like to see another font that has wider letters or perhaps the all-caps like the logo?
Also, I like to spell out "phone" and "fax" but not need an "e" or "email" for the email address.
Also, I would need the words "Registered Investment Advisor" and "Financial Planning & Fee-Only Investments" on the front (I'm looking for a single-sided card). If there's not enough space, can the words "Financial Planning and Wealth Advisors" be removed from the logo graphic to make more room?

```html
<!DOCTYPE html>
<html lang="en">
<head>
<meta charset="utf-8">
<title>Holloway-Prentiss &amp; Associates — Business Cards</title>
<link href="https://fonts.googleapis.com/css2?family=Open+Sans:wght@400;600;700&display=swap" rel="stylesheet">
<style>
  :root {
    --stage: #2e2e2e;
    --card-white: #f7f7f8;
    --card-grey: #e6e7e9;
    --brand-blue: #1a6fd0;
    --brand-blue-deep: #0d4fa6;
    --brand-blue-light: #3d93e8;
    --ink: #222a33;
    --ink-soft: #4a525b;
    --white: #ffffff;
  }
  * { margin: 0; padding: 0; box-sizing: border-box; }
  html, body { width: 1200px; height: 898px; overflow: hidden; }
  body { background: var(--stage); position: relative; font-family: "Open Sans", sans-serif; }

  .card {
    position: absolute;
    width: 516px;
    height: 292px;
    border-radius: 16px;
    overflow: hidden;
  }

  /* Wordmark: name in the text font, one colour, one weight, one plain square */
  .wordmark {
    position: absolute; left: 0; right: 0;
    display: flex; align-items: center; justify-content: center; gap: 10px;
    font-family: "Open Sans", sans-serif; font-weight: 700;
    white-space: nowrap;
  }
  .wordmark__square { display: block; flex: none; }

  /* Front card */
  .card--front { left: 341px; top: 49px; background: linear-gradient(180deg, var(--white) 0%, var(--card-white) 60%, var(--card-grey) 100%); }
  .front__firm { top: 88px; font-size: 19px; color: var(--brand-blue-deep); }
  .front__firm .wordmark__square { width: 14px; height: 14px; background: var(--brand-blue-deep); }
  .front__name {
    position: absolute; left: 0; right: 0; top: 130px;
    text-align: center; font-weight: 700; font-size: 16px;
    letter-spacing: 0.3px; color: var(--brand-blue);
  }
  .front__title {
    position: absolute; left: 0; right: 0; top: 153px;
    text-align: center; font-weight: 700; font-size: 15px; color: var(--ink);
  }
  .front__contact {
    position: absolute; left: 34px; right: 34px; top: 196px;
    display: flex; justify-content: space-between;
    font-size: 11.5px; line-height: 20px; color: var(--ink-soft);
  }
  .front__band { position: absolute; left: 0; right: 0; bottom: 0; height: 56px; }
  .front__band svg { position: absolute; inset: 0; }
  .front__band-text {
    position: absolute; left: 0; right: 0; bottom: 7px;
    text-align: center; color: var(--white);
    font-weight: 700; font-size: 11px; line-height: 15px;
  }

  /* Back card (blue) */
  .card--back {
    left: 58px; top: 406px;
    background: radial-gradient(ellipse at 40% 30%, var(--brand-blue-light) 0%, var(--brand-blue) 45%, var(--brand-blue-deep) 100%);
  }
  .back__firm { top: 98px; font-size: 22px; color: var(--white); }
  .back__firm .wordmark__square { width: 16px; height: 16px; background: var(--white); }
  .back__tagline {
    position: absolute; left: 0; right: 0; top: 188px;
    text-align: center; color: var(--white);
    font-weight: 400; font-size: 16px; letter-spacing: 0.4px;
  }

  /* Logo card (white) */
  .card--logo { left: 635px; top: 406px; background: linear-gradient(160deg, var(--white) 0%, var(--card-white) 55%, var(--card-grey) 100%); }
  .logo__firm { top: 128px; font-size: 26px; color: var(--brand-blue-deep); }
  .logo__firm .wordmark__square { width: 20px; height: 20px; background: var(--brand-blue-deep); }
</style>
</head>
<body>

  <section class="card card--front" aria-label="Card front">
    <div class="wordmark front__firm"><span class="wordmark__square"></span>Holloway-Prentiss &amp; Associates</div>
    <div class="front__name">ELAINE HOLLOWAY-PRENTISS</div>
    <div class="front__title">Principal</div>
    <div class="front__contact">
      <div class="left">372 Orchard Avenue, Suite 485, Larkspur Hills, CA 94099<br>elaine@holloway-prentiss-associates.com</div>
      <div class="right">Phone: 555.240.7182<br>Fax: 555.240.7190</div>
    </div>
    <div class="front__band">
      <svg width="516" height="56" viewBox="0 0 516 56" preserveAspectRatio="none" aria-hidden="true">
        <path d="M0 14 Q258 -4 516 14 L516 56 L0 56 Z" fill="var(--brand-blue-light)"/>
        <path d="M0 20 Q258 2 516 20 L516 56 L0 56 Z" fill="var(--brand-blue)"/>
      </svg>
      <div class="front__band-text">Registered Investment Advisor<br>Financial Planning &amp; Fee-Only Investments</div>
    </div>
  </section>

  <section class="card card--back" aria-label="Card back">
    <div class="wordmark back__firm"><span class="wordmark__square"></span>Holloway-Prentiss &amp; Associates</div>
    <div class="back__tagline">Financial Planning &amp; Fee-Only Investments</div>
  </section>

  <section class="card card--logo" aria-label="Logo card">
    <div class="wordmark logo__firm"><span class="wordmark__square"></span>Holloway-Prentiss &amp; Associates</div>
  </section>

</body>
</html>
```